He Steady Watch Roundtable Podcast is a Top Rated Show dedicated to improving the lives of our brave men and women who serve. Topics about leadership, mental health & resiliency to start living your best life personally and professionally.

Target Market(s)

First Responder Community - Law Enforcement, EMS, Fire Department, Military

Industry/Entity Type

First Responder Community

Requirements
Must have
• I would like my picture and logo to be part of the design. This needs to be formatted for Kestrel Casts and other platforms
Nice to have
• Some style. Modern Look
Should not have
• N/A

```html
<!DOCTYPE html>
<html lang="en">
<head>
<meta charset="utf-8">
<title>Steady Watch Roundtable Podcast — Cover Art</title>
<link rel="stylesheet" href="https://fonts.googleapis.com/css2?family=Russo+One&family=Montserrat:wght@600;800&display=swap">
<style>
  :root {
    --sky-blue: #5aaee3;
    --photo-blue: #4c9ad0;
    --night: #0c0c0c;
    --white: #ffffff;
    --capsule-light: #f2f6f9;
    --capsule-shade: #c9dceb;
  }
  html, body {
    margin: 0;
    padding: 0;
    width: 1200px;
    height: 1200px;
    overflow: hidden;
    background: var(--white);
  }
  .cover {
    display: block;
    width: 1200px;
    height: 1200px;
  }
  .panel-blue { fill: var(--sky-blue); }
  .panel-dark { fill: var(--night); }
  .host-photo { fill: url(#hostPhotoTone); }
  .mic-capsule-fill { fill: url(#capsuleTone); }
  .mic-line {
    fill: none;
    stroke: var(--sky-blue);
    stroke-width: 14;
    stroke-linecap: butt;
  }
  .podcast-label {
    font-family: "Montserrat", sans-serif;
    font-weight: 600;
    font-size: 38px;
    letter-spacing: 18px;
    fill: var(--white);
  }
  .show-name {
    font-family: "Russo One", sans-serif;
    font-size: 112px;
    fill: var(--white);
  }
  .show-subtitle {
    font-family: "Russo One", sans-serif;
    font-size: 34px;
    fill: var(--sky-blue);
    letter-spacing: 1px;
  }
  .show-topics {
    font-family: "Montserrat", sans-serif;
    font-weight: 800;
    font-size: 33px;
    fill: var(--white);
  }
  .topic-star { fill: var(--sky-blue); }
</style>
</head>
<body>
<svg class="cover" viewBox="0 0 1200 1200" xmlns="http://www.w3.org/2000/svg">
  <defs>
    <linearGradient id="hostPhotoTone" x1="0" y1="0" x2="0" y2="1">
      <stop offset="0" stop-color="#62b2e6"/>
      <stop offset="1" stop-color="#4a95ca"/>
    </linearGradient>
    <linearGradient id="capsuleTone" x1="0" y1="0" x2="0" y2="1">
      <stop offset="0" stop-color="var(--capsule-light)"/>
      <stop offset="1" stop-color="var(--capsule-shade)"/>
    </linearGradient>
    <path id="podcastArc" d="M 668 330 A 210 210 0 0 1 1078 330"/>
  </defs>

  <!-- background split -->
  <rect class="panel-blue" x="0" y="0" width="1200" height="1200"/>
  <polygon class="host-photo" role="img" aria-label="Photo of the show host in a dark button-up shirt, tinted blue"
           points="60,0 960,0 960,366 60,871"/>
  <polygon class="panel-dark" points="0,905 1200,231 1200,1200 0,1200"/>

  <!-- microphone emblem -->
  <g class="mic-emblem">
    <text class="podcast-label"><textPath href="#podcastArc" startOffset="50%" text-anchor="middle">PODCAST</textPath></text>
    <rect class="mic-capsule-fill" role="img" aria-label="Drawn portrait of the show host"
          x="744" y="254" width="258" height="311" rx="129"/>
    <rect class="mic-line" x="744" y="254" width="258" height="311" rx="129" stroke-width="6"/>
    <path class="mic-line" d="M 683 470 V 520 A 190 190 0 0 0 1063 520 V 470"/>
    <line class="mic-line" x1="873" y1="710" x2="873" y2="803"/>
    <line class="mic-line" x1="780" y1="803" x2="966" y2="803"/>
  </g>

  <!-- show title -->
  <g class="show-title">
    <text class="show-name" x="600" y="990" text-anchor="middle" textLength="880" lengthAdjust="spacingAndGlyphs">STEADY WATCH</text>
    <text class="show-subtitle" x="600" y="1036" text-anchor="middle">ROUNDTABLE PODCAST</text>
    <text class="show-topics" x="600" y="1086" text-anchor="middle" textLength="890" lengthAdjust="spacingAndGlyphs">LEADERSHIP<tspan class="topic-star">★</tspan>COACHING<tspan class="topic-star">★</tspan>PERSONAL DEVELOPMENT</text>
  </g>
</svg>
</body>
</html>
```